Stationery Design Project

We need a stationery design to change our look to a more corporate design. My company has been established since 1989 and over that time has changed from your average sign company to doing more Corporate re branding projects and have some multi National clients.
Our website is currently being redesigned so we need a new logo and business cards etc. to compliment it.
I have 2 graphic designers employed but i want on outsiders opinion and a totally independant view point.
Updates
Hi Designers
We are predominantely a sign manufacturing company that manufacturers every type of sign you can imagine. However the majoprity of our work is digital graphics. Our claim to faim is that we wrap the Harbour Skytrams and Glidetrams which everyone seems to know in Sydney.We also do all sorts of Large format digital printing, vehicle wraps,vinyl signage,LED & Neon Illuminated signage,CNC Routing all materials,Laser cutting and Engraving, Architectural signage, Cut Out letters and Screenprinting.
Aswell as this we totally re-brand companies with internal wall graphics reception signage way finding signage and the like.We are a medium size company that has been trading since 1989 and has some very large reputable clients.
Our Company name is Brightmark Pty Ltd but like to have Signage and Graphics in our stationery.
Our details are as follows T: 9381 5027 F: 9381 5063 Unit 4, 22 Quarry Lane.Pine Flats. NSW 2163 email mail@brightmarkexample.com our current website is being re-designed www.brightmarkexample.com
The design and colour scheme i would like is quite simple with a corporate feel and blue, grey & magenta are colours that seem to suit but am open to most suggestions just looking for clean lines.
Hopefully this is enough information if you require any more please ask.
Regards Neil Barrowby
We are looking to simplify our LOGO not too concerned yet about layout of stationery items that we can easily work on later. I want to get a new logo that we can work with before we return to work on the 16th January so please concentrate on just the logo for now.
We would like to have Signs & Graphics somewhere in the name even though our registered name is Brightmark Pty Ltd. Brightmark is one word, i want it to be quite a bold font with no seriffs.The bright blue and grey colours are favourites so far with maybe a little magenta added later. Would like to have a Logo that is totally seperate and then the Brightmark P/L Signs & graphics as a secondary item just to let people know what Brightmark do as the name obviously does not say what we are about.
Also we need to consider how we can put logo on T-shirts work shirts and company vehicles.
We do not need CD cover or envelopes but letterheads and business cards.
Industry/Entity Type
Business
Look and feel
Each slider illustrates characteristics of the customer's brand and the style your logo design should communicate.

```html
<!DOCTYPE html>
<html lang="en">
<head>
<meta charset="utf-8">
<title>Brightmark Signs – Stationery</title>
<link rel="stylesheet" href="https://fonts.googleapis.com/css2?family=Open+Sans:wght@400;600&display=swap">
<style>
  :root {
    --ink: #333333;
    --paper: #ffffff;
    --card-grey: #f1f1f1;
    --brand-blue: #00a0c6;
    --edge: #9a9a9a;
    --shadow: rgba(0, 0, 0, 0.55);
  }
  html, body {
    margin: 0;
    padding: 0;
    overflow: hidden;
  }
  body {
    font-family: "Open Sans", sans-serif;
    color: var(--ink);
    background: var(--paper);
  }
  .canvas {
    position: relative;
    width: 1200px;
    height: 856px;
    overflow: hidden;
    background: var(--paper);
  }
  .sheet {
    position: absolute;
    box-sizing: border-box;
    box-shadow: 6px 6px 6px var(--shadow);
  }
  .wordmark {
    position: absolute;
    margin: 0;
    font-weight: 400;
    line-height: 1;
    white-space: nowrap;
    color: var(--ink);
    letter-spacing: -0.5px;
  }

  /* Letterhead */
  .letterhead {
    left: 76px;
    top: 70px;
    width: 506px;
    height: 719px;
    background: var(--paper);
  }
  .letterhead .wordmark {
    left: 25px;
    top: 48px;
    font-size: 42px;
  }

  /* Contact footer shared by letterhead and envelope */
  .contact {
    position: absolute;
    font-size: 11px;
    letter-spacing: 1px;
    line-height: 15px;
  }
  .contact-row {
    display: flex;
    justify-content: space-between;
  }
  .letterhead .contact {
    left: 34px;
    top: 664px;
    width: 440px;
  }

  /* Business card front */
  .card-front {
    left: 605px;
    top: 72px;
    width: 205px;
    height: 130px;
    background: var(--card-grey);
  }
  .card-front .wordmark {
    left: 24px;
    top: 56px;
    font-size: 18px;
  }

  /* Business card back */
  .card-back {
    left: 605px;
    top: 220px;
    width: 205px;
    height: 130px;
    background: var(--brand-blue);
    color: var(--paper);
    padding: 9px 11px;
    font-size: 9px;
    line-height: 12.5px;
  }
  .card-back .person-name {
    font-weight: 600;
    margin: 0;
  }
  .card-back p {
    margin: 0;
  }

  /* Envelope */
  .envelope {
    left: 605px;
    top: 369px;
    width: 506px;
    height: 193px;
    background: var(--paper);
    border: 1px solid var(--edge);
  }
  .envelope .wordmark {
    left: 19px;
    top: 33px;
    font-size: 29px;
  }
  .envelope .contact {
    left: 19px;
    top: 154px;
    width: 466px;
  }
</style>
</head>
<body>
<div class="canvas">

  <section class="sheet letterhead" aria-label="Letterhead">
    <h1 class="wordmark">BRIGHTMARK SIGNS</h1>
    <div class="contact">
      <div class="contact-row">
        <span>Brightmark Signs</span><span>Unit 4</span><span>22 Quarry Lane</span><span>Pine Flats</span><span>NSW 2163</span>
      </div>
      <div class="contact-row">
        <span>Tel: 9381 5027</span><span>Fax: 9381 5063</span><span>Email: mail@brightmarkexample.com</span>
      </div>
    </div>
  </section>

  <section class="sheet card-front" aria-label="Business card front">
    <div class="wordmark">BRIGHTMARK SIGNS</div>
  </section>

  <section class="sheet card-back" aria-label="Business card back">
    <p class="person-name">NEIL BARROWBY</p>
    <p>job title</p>
    <p>neil@brightmarkexample.com</p>
    <p>9381 5027</p>
  </section>

  <section class="sheet envelope" aria-label="Envelope">
    <div class="wordmark">BRIGHTMARK SIGNS</div>
    <div class="contact">
      <div class="contact-row">
        <span>Brightmark Signs</span><span>Unit 4</span><span>22 Quarry Lane</span><span>Pine Flats</span><span>NSW 2163</span>
      </div>
      <div class="contact-row">
        <span>Tel: 9381 5027</span><span>Fax: 9381 5063</span><span>Email: mail@brightmarkexample.com</span>
      </div>
    </div>
  </section>

</div>
</body>
</html>
```